Social Media Graphics - ALL TEXT RK

We are looking for a series of social media graphics for Instagram (standard size 1:1 (1080x1080px) that are ALL TEXT. We want the following quotes below on each graphic; one quote per graphic. AND, In very small letters at the bottom of each graphic, add @RKMarlowLive

The look and feel of these graphics should be complimentary to the color palette attached below; but keep them simple. But the design is up to you; at the end of this document, I provided various samples of all text graphics that I like as examples.

Target Market(s)

women looking to lose weight

Industry/Entity Type

health and wellness

Colors
E54698
E96AAD
F1A4CE
F9D9EA
FCEFF6

Requirements
Must have
• the quotes in the document
Should not have
• no stock photography

```html
<!DOCTYPE html>
<html lang="en">
<head>
<meta charset="utf-8">
<title>Natural Solution – RK Marlow</title>
<link href="https://fonts.googleapis.com/css2?family=Oswald:wght@600;700&display=swap" rel="stylesheet">
<style>
  :root {
    --pink-deep: #ff1289;
    --pink-mid: #ff2e95;
    --pink-light: #ff5aa8;
    --shape-tint: rgba(200, 40, 140, 0.22);
    --shape-tint-soft: rgba(255, 120, 180, 0.18);
    --white: #ffffff;
  }
  html, body {
    margin: 0;
    padding: 0;
    width: 1200px;
    height: 1200px;
    overflow: hidden;
    background: var(--pink-deep);
  }
  .quote-card {
    position: relative;
    width: 1200px;
    height: 1200px;
    background:
      radial-gradient(circle at 88% 8%, var(--pink-light) 0%, rgba(255, 90, 168, 0) 55%),
      linear-gradient(135deg, var(--pink-deep) 0%, var(--pink-mid) 60%, var(--pink-deep) 100%);
  }
  .quote-card svg {
    position: absolute;
    inset: 0;
  }
  .bracket {
    fill: none;
    stroke: var(--white);
    stroke-width: 5.5;
  }
  .accent-shape { fill: var(--shape-tint); }
  .accent-shape-soft { fill: var(--shape-tint-soft); }
  .quote-line {
    font-family: "Oswald", "Arial Narrow", sans-serif;
    font-weight: 700;
    fill: var(--white);
    text-anchor: middle;
  }
  .handle {
    font-family: "Oswald", "Arial Narrow", sans-serif;
    font-weight: 600;
    fill: var(--white);
    text-anchor: middle;
    font-size: 31px;
  }
</style>
</head>
<body>
<main class="quote-card">
  <svg width="1200" height="1200" viewBox="0 0 1200 1200" xmlns="http://www.w3.org/2000/svg">
    <g class="accent-shapes">
      <rect class="accent-shape-soft" x="930" y="520" width="260" height="260" transform="rotate(45 1060 650)"/>
      <rect class="accent-shape" x="1000" y="590" width="150" height="150" transform="rotate(45 1075 665)"/>
      <rect class="accent-shape-soft" x="760" y="780" width="300" height="300" transform="rotate(45 910 930)"/>
      <rect class="accent-shape" x="1020" y="900" width="260" height="260" transform="rotate(45 1150 1030)"/>
    </g>

    <path class="bracket" d="M283 176 H133 V1024 H283"/>
    <path class="bracket" d="M917 176 H1070 V1024 H917"/>

    <g class="quote">
      <text class="quote-line" x="600" y="391" font-size="108" textLength="406" lengthAdjust="spacingAndGlyphs">FINALLY-A</text>
      <text class="quote-line" x="600" y="483" font-size="66" textLength="661" lengthAdjust="spacingAndGlyphs">NATURAL SOLUTION</text>
      <text class="quote-line" x="600" y="561" font-size="60" textLength="455" lengthAdjust="spacingAndGlyphs">THAT FLATTENS</text>
      <text class="quote-line" x="600" y="681" font-size="80" textLength="394" lengthAdjust="spacingAndGlyphs">YOUR BELLY</text>
      <text class="quote-line" x="600" y="778" font-size="76" textLength="372" lengthAdjust="spacingAndGlyphs">AND EASES</text>
      <text class="quote-line" x="600" y="883" font-size="90" textLength="655" lengthAdjust="spacingAndGlyphs">STOMACH BLOAT</text>
    </g>

    <text class="handle" x="600" y="1036" textLength="286" lengthAdjust="spacingAndGlyphs">@RKMarlowLive</text>
  </svg>
</main>
</body>
</html>
```